Health Information/Education Logo Design

We need a logo design for a new company based in Atlanta called Meadowlark Health. The program is about patient empowerment. We provide health information and education on how to get healthy, stay healthy, and how to be proactive in your care. We also provide medication and injection training to help patients feel their best and to ensure successful therapy outcomes.
We like the colors yellow, pink, teal and purple and would like to see some or all of these colors in the designs. The final design should communicate caring, considerate, compassionate information, education and training services
Industry/Entity Type
Education
Contact Information for Business Card
Meadowlark Health
Danielle Ostrander RN, MSN, MHA
Nurse Educator
555.214.3096 cell
555.470.2283 fax

```html
<!DOCTYPE html>
<html lang="en">
<head>
<meta charset="utf-8">
<title>Meadowlark Health – Business Card</title>
<link rel="stylesheet" href="https://fonts.googleapis.com/css2?family=Open+Sans:wght@400;600&display=swap">
<style>
  :root {
    --page-bg: #ece8ee;
    --card-light: #a44eb3;
    --card-mid: #7d2a8c;
    --card-dark: #561160;
    --accent-yellow: #f3e51c;
    --mark-teal: #1f9a8e;
  }
  * { margin: 0; padding: 0; box-sizing: border-box; }
  html, body {
    width: 1200px;
    height: 900px;
    overflow: hidden;
    background: var(--page-bg);
    font-family: "Open Sans", sans-serif;
  }
  .business-card {
    position: absolute;
    left: 100px;
    top: 164px;
    width: 1000px;
    height: 572px;
    border-radius: 6px;
    background: linear-gradient(160deg, var(--card-light) 0%, var(--card-mid) 50%, var(--card-dark) 100%);
    box-shadow: 0 18px 40px rgba(40, 10, 45, 0.35);
    overflow: hidden;
    color: var(--accent-yellow);
  }
  .divider-line {
    position: absolute;
    inset: 0;
    width: 1000px;
    height: 572px;
  }
  .brand-mark {
    position: absolute;
    left: 70px;
    top: 268px;
    display: flex;
    align-items: center;
    gap: 12px;
    font-weight: 600;
    font-size: 22px;
  }
  .brand-mark__square {
    width: 38px;
    height: 38px;
    background: var(--mark-teal);
  }
  .company-name {
    position: absolute;
    left: 410px;
    top: 150px;
    font-weight: 600;
    font-size: 64px;
    line-height: 1;
    letter-spacing: 0.5px;
  }
  .person-name {
    position: absolute;
    left: 470px;
    top: 372px;
    font-weight: 600;
    font-size: 40px;
    line-height: 1;
  }
  .person-credentials {
    position: absolute;
    left: 470px;
    top: 424px;
    font-weight: 400;
    font-size: 25px;
    line-height: 1;
  }
  .contact-numbers {
    position: absolute;
    left: 560px;
    top: 470px;
    width: 280px;
    text-align: center;
    font-weight: 400;
    font-size: 29px;
    line-height: 40px;
    list-style: none;
  }
</style>
</head>
<body>
  <main class="business-card">
    <svg class="divider-line" viewBox="0 0 1000 572" aria-hidden="true">
      <line x1="0" y1="440" x2="1000" y2="200" stroke="var(--accent-yellow)" stroke-width="4"/>
    </svg>

    <div class="brand-mark">
      <span class="brand-mark__square"></span>
      <span>Meadowlark Health</span>
    </div>

    <h1 class="company-name">Meadowlark Health</h1>

    <h2 class="person-name">Danielle Ostrander</h2>
    <p class="person-credentials">RN, MSN, MHA Nurse Educator</p>

    <ul class="contact-numbers">
      <li>555.214.3096</li>
      <li>555.470.2283</li>
    </ul>
  </main>
</body>
</html>
```